Letterhead

We need a professional, compelling letterhead that can be used for print and email stationary. We have the logo and the letterhead styling and colors should blend seamlessly and be complimentary. Looking for something unique and thoughtful.
Updates

Reason: There are good ideas and am requesting changes to some ideas in order to make a final decision. Thank you for for submissions. Also, I have uploaded the ai file. Please use that file. Thank you.

If you cannot see the .ai version of the logo that I have tried to upload, please message me if you want to make changes to your submission or submit new design and I will send that file to you directly. This .ai will need to be used in order to ensure high quality printing. Thank you.

Target Market(s)

Clients. Business partners.

Industry/Entity Type

It Professional

Requirements
Must have
• Our logo incorporated. Also the phrase, or tag line - where business thrives.
Should not have
• Not boring. Not typical. Not too busy.

```html
<!DOCTYPE html>
<html lang="en">
<head>
<meta charset="utf-8">
<title>Meridian Advisory Group LLC — Stationery</title>
<link rel="stylesheet" href="https://fonts.googleapis.com/css2?family=Open+Sans:wght@400;600&display=swap">
<style>
  :root {
    --navy: #1f2d5c;
    --navy-soft: #2a3a72;
    --green: #2e9b45;
    --paper: #ffffff;
    --ink: #3a3a3a;
    --muted: #8a8f99;
    --stage: #e9e9ec;
    --watermark: #f1f1f1;
  }
  * { box-sizing: border-box; margin: 0; padding: 0; }
  html, body { width: 1200px; height: 675px; overflow: hidden; background: var(--stage); }
  body { font-family: "Open Sans", Arial, sans-serif; color: var(--ink); position: relative; }

  .folder {
    position: absolute; left: 150px; top: 50px; width: 404px; height: 575px;
    background: var(--navy);
    box-shadow: 0 6px 18px rgba(0,0,0,.18);
  }
  .folder-mark {
    position: absolute; left: 102px; top: 187px; width: 200px; height: 200px;
    border-radius: 50%; background: var(--navy-soft);
  }

  .letterhead {
    position: absolute; left: 626px; top: 50px; width: 406px; height: 575px;
    background: var(--paper); overflow: hidden;
    box-shadow: 0 6px 18px rgba(0,0,0,.18);
  }
  .brand {
    position: absolute; right: 26px; top: 24px;
    display: flex; align-items: center; gap: 8px;
    border-bottom: 2px solid var(--green); padding-bottom: 5px;
  }
  .brand-dot { width: 18px; height: 18px; border-radius: 50%; background: var(--navy); }
  .brand-name { font-weight: 600; font-size: 11px; color: var(--navy); letter-spacing: .04em; }

  .watermark {
    position: absolute; left: 118px; top: 168px; width: 190px; height: 190px;
    border-radius: 50%; background: var(--watermark);
  }

  .web {
    position: absolute; left: 30px; top: 80px;
    display: flex; align-items: center; gap: 5px;
    font-size: 8px; font-weight: 600; color: var(--navy);
  }
  .web-dot { width: 7px; height: 7px; border-radius: 50%; background: var(--green); }

  .letter { position: absolute; left: 30px; top: 112px; width: 346px; font-size: 7.4px; line-height: 1.55; }
  .letter p { margin-bottom: 9px; }
  .signature {
    width: 90px; height: 26px; margin-top: 4px;
    background: linear-gradient(90deg, #e4e4e8, #f3f3f5);
  }

  .footer {
    position: absolute; left: 0; right: 0; bottom: 0; height: 34px;
    background: var(--paper);
    border-bottom: 8px solid var(--navy);
    box-shadow: inset 0 -3px 0 var(--green);
    display: flex; align-items: center; gap: 12px; padding: 0 14px 2px;
    font-size: 7px; color: var(--navy);
  }
  .footer-name { font-weight: 600; margin-right: auto; }
  .contact { display: flex; align-items: center; gap: 3px; }
  .contact svg { width: 8px; height: 8px; fill: var(--green); }
</style>
</head>
<body>
  <section class="folder" aria-label="Presentation folder">
    <div class="folder-mark" role="img" aria-label="Faint circular company emblem"></div>
  </section>

  <article class="letterhead">
    <div class="watermark" role="img" aria-label="Faint circular company emblem"></div>

    <header class="brand">
      <span class="brand-dot"></span>
      <span class="brand-name">Meridian Advisory Group LLC</span>
    </header>

    <div class="web"><span class="web-dot"></span>www.meridianadvisoryllc.com</div>

    <div class="letter">
      <p>Dear Folks</p>
      <p>Lorem ipsum dolor sit amet, consectetur adipiscing elit. Quisque dictum leo quis mauris dictum auctor. Praesent viverra, elit at rutrum fringilla, purus nisi feugiat est, sit amet lobortis magna mauris id nibh. Sed interdum massa non mauris faucibus cursus. Integer at tellus sit amet lacus ultrices ullamcorper. Nunc vel libero dui, sit amet pellentesque ligula. Suspendisse semper, urna.</p>
      <p>Aenean quis nisi arcu, blandit mollis odio. Vestibulum nulla enim, viverra a auctor quis, suscipit rhoncus libero. Donec quis libero vel magna luctus pulvinar. Duis eget nulla vel massa commodo semper placerat id leo. Nunc eu leo sed quam hendrerit accumsan. Maecenas eleifend nisi non velit dignissim ut suscipit arcu imperdiet. Phasellus nisi nulla, tincidunt. Proin tincidunt, est sed rhoncus mattis, nunc sem aliquet quam, eget tristique augue dolor vel orci. Vestibulum et tellus dui, vitae sollicitudin sapien. Pellentesque nisl tortor, faucibus in mollis non, dignissim et felis.</p>
      <p>Phasellus nisi nulla, tincidunt. Proin tincidunt, est sed rhoncus mattis, nunc sem aliquet quam, eget tristique augue dolor vel orci. Vestibulum et tellus dui, vitae sollicitudin sapien. Pellentesque nisl tortor, faucibus in mollis non, dignissim et felis.</p>
      <p>Sincerely,</p>
      <p>Good Looking</p>
      <div class="signature" role="img" aria-label="Handwritten signature of Dana Whitfield"></div>
    </div>

    <footer class="footer">
      <span class="footer-name">Meridian Advisory Group LLC</span>
      <span class="contact">
        <svg viewBox="0 0 10 10"><path d="M2 1h2l1 2.5-1.3 1a6 6 0 0 0 2.8 2.8l1-1.3L10 7v2a1 1 0 0 1-1 1A9 9 0 0 1 1 2a1 1 0 0 1 1-1z"/></svg>
        T: (206) 555-0142
      </span>
      <span class="contact">
        <svg viewBox="0 0 10 10"><path d="M2 0h5v3H2zM0 3.5h10V8H8v2H2V8H0zM3 7v2h4V7z"/></svg>
        F: (425) 555-0187
      </span>
      <span class="contact">
        <svg viewBox="0 0 10 10"><path d="M0 2h10v6H0zM1 3v.3l4 2.5 4-2.5V3L5 5.3z"/></svg>
        info@meridianadvisoryllc.com
      </span>
    </footer>
  </article>
</body>
</html>
```